Dr. Pelham Billboard Sign Design

Family Dental Practice looking for a billboard sign design. We have Attached a Image of Dr Pelham and Her horse she would like to incorporate. The size of the sign is 118" tall and 196" Wide. We hired a previous designer to work on this also but would like to see what other come up with before we decide on a final. Please use something similar for a animal shelter icon to go beside the Animal Shelter Discount statement. You can use the text from the postcard file attached. I know text adjustments will be needed, but more interested in a eye catching design. Themes: Fall/Winter/Mountains/Nature , colors: open but Dr P like purple. We are open to ideas and will answer any questions.
TEXT
Theme: Fall/Winter/Mountain
Image: Dr Pelham with Horse (Same from mailer design)
Text to Keep that needs to be bold and Priority
1. Dr. Rosalind Pelham Family Dentistry
314 Brellin Court Spruce Pine, NC 28094
828-413-5276 | RPelhamDDS@Velmorx.net
(FaceBook icon) RosalindPelhamDDS
2. ACCEPTING NEW PATIENTS
3. Affordable Dentistry for Your Whole Family
4. WE FILE YOUR INSURANCE CLAIMS
5. Discounts for Senior Citizens, Law Enforcement, First Responders, Military Personnel, State Employees and College Students
6. (Cool Animal Shelter Icon) WE OFFER A DISCOUNT TO PATIENTS WHO SUPPORT OUR LOCAL ANIMAL SHELTERS BY ADOPTING, DONATING OR VOLUNTEERING
7. Schedule Your Appointment TODAY!
Target Market(s)
Local Community to Bring in Patients to dental office
Industry/Entity Type
Dental
Look and feel

```html
<!DOCTYPE html>
<html lang="en">
<head>
<meta charset="utf-8">
<title>Dr. Pelham Billboard</title>
<link rel="stylesheet" href="https://fonts.googleapis.com/css2?family=Montserrat:wght@500;600;700&family=Questrial&display=swap">
<style>
  :root {
    --page: #ffffff;
    --panel: #a9a6d4;
    --ridge-far: #9c98cb;
    --ridge-near: #8f89c2;
    --accent: #6e2c8f;
    --ink: #ffffff;
    --social: #4a5aa8;
    --photo-dark: #5a3b2c;
    --photo-mid: #8a6a55;
    --photo-tint: #a3508f;
  }
  html, body {
    margin: 0;
    width: 1200px;
    height: 1200px;
    overflow: hidden;
    background: var(--page);
  }
  .billboard {
    position: absolute;
    left: 27px;
    top: 255px;
    width: 1147px;
    height: 690px;
  }
  .caps {
    font-family: "Montserrat", "Century Gothic", sans-serif;
    font-weight: 600;
    font-variant: small-caps;
    fill: var(--ink);
  }
  .sans {
    font-family: "Questrial", "Century Gothic", sans-serif;
    fill: var(--ink);
  }
  .accent { fill: var(--accent); }
  .rule { fill: var(--accent); }
</style>
</head>
<body>
<svg class="billboard" viewBox="0 0 1147 690" xmlns="http://www.w3.org/2000/svg">
  <defs>
    <linearGradient id="photoTone" x1="0" y1="0" x2="1" y2="0.3">
      <stop offset="0" stop-color="var(--photo-mid)"/>
      <stop offset="0.35" stop-color="var(--photo-dark)"/>
      <stop offset="0.7" stop-color="var(--photo-tint)"/>
      <stop offset="1" stop-color="#b56aa6"/>
    </linearGradient>
    <clipPath id="panelShape">
      <polygon points="389,0 1147,0 1147,690 905,690"/>
    </clipPath>
  </defs>

  <rect class="portrait-photo" x="0" y="0" width="1147" height="690" fill="url(#photoTone)"
        role="img" aria-label="Photo of Dr. Pelham standing beside her bay horse with a white blaze, in a fall pasture with a purple tint"/>

  <g class="info-panel" clip-path="url(#panelShape)">
    <rect x="0" y="0" width="1147" height="690" fill="var(--panel)"/>
    <polygon class="mountain-ridge-far" fill="var(--ridge-far)"
             points="700,690 700,640 790,600 860,625 950,585 1030,615 1100,590 1147,605 1147,690"/>
    <polygon class="mountain-ridge-near" fill="var(--ridge-near)"
             points="700,690 700,665 800,640 880,655 980,630 1070,650 1147,638 1147,690"/>
  </g>

  <g class="headline caps" text-anchor="end" font-size="28">
    <text x="1127" y="45" textLength="680" lengthAdjust="spacingAndGlyphs">Straight From The Horses Mouth DR. PELHAM</text>
    <text x="1115" y="81" textLength="620" lengthAdjust="spacingAndGlyphs">Is Your Best Choice For Dental Health!</text>
  </g>
  <rect class="rule" x="479" y="93" width="624" height="4"/>

  <text class="practice-name caps" x="1127" y="135" text-anchor="end" font-size="22" textLength="470" lengthAdjust="spacingAndGlyphs">Dr. Rosalind Pelham Family Dentistry</text>

  <g class="contact caps" text-anchor="end" font-size="20" font-weight="500">
    <text x="1127" y="172" textLength="175" lengthAdjust="spacingAndGlyphs">828-413-5276</text>
    <text x="1127" y="198" textLength="300" lengthAdjust="spacingAndGlyphs">RPelhamDDS@Velmorx.net</text>
    <text x="1127" y="224" textLength="262" lengthAdjust="spacingAndGlyphs">RosalindPelhamDDS</text>
  </g>
  <rect class="social-square" x="843" y="209" width="16" height="16" fill="var(--social)"/>
  <rect class="rule" x="865" y="232" width="262" height="2.5"/>

  <text class="address caps" x="1127" y="272" text-anchor="end" font-size="21" textLength="520" lengthAdjust="spacingAndGlyphs">314 Brellin Court Spruce Pine, NC 28094</text>

  <text class="tagline caps" x="1127" y="314" text-anchor="end" font-size="18" font-weight="500" textLength="420" lengthAdjust="spacingAndGlyphs">Affordable Dentistry for Your Whole Family</text>

  <text class="new-patients sans" x="1127" y="375" text-anchor="end" font-size="25" letter-spacing="0.5">ACCEPTING <tspan class="accent">NEW</tspan> PATIENTS</text>
  <rect class="rule" x="757" y="386" width="370" height="3.5"/>

  <text class="insurance sans" x="1127" y="425" text-anchor="end" font-size="18" letter-spacing="0.5">WE FILE YOUR INSURANCE CLAIMS</text>

  <text class="schedule caps" x="1127" y="475" text-anchor="end" font-size="15">Schedule Your Appointment <tspan class="accent">TODAY!</tspan></text>

  <g class="paw-icon" fill="#ffffff">
    <ellipse cx="882" cy="563" rx="20" ry="15"/>
    <ellipse cx="858" cy="543" rx="7" ry="9"/>
    <ellipse cx="872" cy="528" rx="7.5" ry="10"/>
    <ellipse cx="892" cy="528" rx="7.5" ry="10"/>
    <ellipse cx="906" cy="543" rx="7" ry="9"/>
  </g>

  <text class="shelter-discount sans" x="921" y="553" font-size="15.5">DISCOUNT FOR <tspan class="accent">SUPPORT</tspan></text>
  <text class="shelter-discount sans" x="1029" y="573" text-anchor="middle" font-size="12.5">TO LOCAL SHELTERS</text>

  <text class="discount-list caps" x="15" y="681" font-size="12" textLength="1116" lengthAdjust="spacingAndGlyphs">Discounts for Senior Citizens, Law Enforcement, First Responders, Military Personnel, State Employees and College Students</text>
</svg>
</body>
</html>
```